Web Design Project

We have screen protector brand for mobile phone and we need
Looking for talented web designer. We need only graphic design of 3 page design Home, Catalog page and Product page

- Home page
- There will be rotating banners on the home page
- Top menu will have Hot products, Screen Protectors, Videos, Contact us
- Screen Protectors will be submenu
- Website will be two languages so put US and Turkish flags on the corner so users will be able to switch
- Home page, there will be newest products and hot products and also one video

I also live any additional creative idea for the website
There will be one inner page and catalog page

Check existing page www.durvelo.com which looks pretty bad. You can take logo from there. If you need logo separate i can send it.

I have attached the layout but feel free to change it. I only try to give idea what i wanna see on it.

```html
<!DOCTYPE html>
<html lang="en">
<head>
<meta charset="utf-8">
<title>Durvelo — Home</title>
<link rel="stylesheet" href="https://fonts.googleapis.com/css2?family=PT+Sans:wght@400;700&display=swap">
<style>
:root{
  --orange:#f07406;
  --orange-light:#f78b22;
  --orange-dark:#d65f00;
  --ink:#222;
  --ink-soft:#3a3a3a;
  --page:#ffffff;
  --backdrop:#d9d9d9;
  --footer:#efefef;
  --rule:#d6d6d6;
}
*{box-sizing:border-box;margin:0;padding:0}
html,body{width:1037px;height:1200px;overflow:hidden}
body{background:var(--backdrop);font-family:"PT Sans",Arial,sans-serif;color:var(--ink)}
.stage{position:relative;width:1200px;height:1390px;transform:scale(.8642);transform-origin:0 0;
  background:linear-gradient(90deg,#fff 0,#e4e4e4 8%,#cfcfcf 11.4%,#fff 11.45%,#fff 88.55%,#cfcfcf 88.6%,#e4e4e4 92%,#fff 100%)}
.abs{position:absolute}
.lines{white-space:nowrap}
.logo{left:160px;top:26px;display:flex;align-items:center;gap:12px}
.logo-mark{width:34px;height:34px;background:var(--orange)}
.logo-name{font-size:44px;font-weight:400;color:#3b3b3b;letter-spacing:2px;text-transform:uppercase}
.search{left:925px;top:47px;width:120px;height:22px;background:linear-gradient(var(--orange-light),var(--orange));border:1px solid #e2e2e2;border-radius:2px}
.search svg,.newsletter-input svg{position:absolute;right:5px;top:5px}
.nav{left:156px;top:97px;width:890px;height:46px;border-radius:6px;background:linear-gradient(var(--orange-light),var(--orange) 55%,var(--orange-dark));box-shadow:0 2px 3px rgba(0,0,0,.25)}
.nav a{position:absolute;top:0;height:46px;line-height:46px;color:#fff;font-size:13px;text-decoration:none}
.nav a.active{background:linear-gradient(#4b4b4b,#2e2e2e);padding:0 9px}
.newsletter-input{left:787px;top:153px;width:118px;height:22px;background:var(--orange);border:1px solid #e2e2e2;font-size:9px;color:#f9b97a;padding:3px 4px}
.newsletter-btn{left:925px;top:153px;width:118px;height:22px;background:linear-gradient(#fff,#e9e9e9);border:1px solid #cfcfcf;font-size:10.5px;color:var(--orange);text-align:center;line-height:20px}
.banner-frame{left:156px;top:183px;width:890px;height:412px;background:#fff;box-shadow:0 1px 3px rgba(0,0,0,.2)}
.banner{left:161px;top:187px;width:880px;height:402px;background:linear-gradient(160deg,#f48a1c,var(--orange) 50%,#ea6a00)}
.banner h1{position:absolute;left:59px;top:70px;font-size:43px;font-weight:400;color:#fff}
.banner p{position:absolute;left:59px;top:176px;font-size:12.5px;line-height:15.6px;color:#2a1a0a}
.btn-download{position:absolute;left:58px;top:250px;width:94px;height:30px;border-radius:5px;background:linear-gradient(#fff,#e4e4e4);border:1px solid #ccc;font-size:11px;color:var(--orange);text-align:center;line-height:28px}
.banner-art{position:absolute;left:550px;top:45px;width:310px;height:330px;background:linear-gradient(160deg,rgba(40,130,200,.0) 0,rgba(30,110,180,.55) 30%,rgba(25,80,130,.55) 60%,rgba(240,116,6,0) 95%)}
.banner-shadow{left:130px;top:592px;width:940px;height:26px;background:radial-gradient(ellipse at 50% 0,rgba(0,0,0,.45),rgba(0,0,0,0) 70%)}
.strip{left:156px;top:618px;width:890px;height:114px;background:#fff;box-shadow:0 1px 3px rgba(0,0,0,.2)}
.strip-inner{left:160px;top:622px;width:880px;height:104px;background:var(--orange)}
.tile{position:absolute;top:637px;height:74px;border:3px solid #fff}
.tile.arrow{width:54px;display:flex;align-items:center;justify-content:center}
.tile.thumb{width:129px}
.tile.thumb span{position:absolute;left:32px;top:8px;width:60px;height:52px;border-radius:4px;background:linear-gradient(135deg,#9ccf2c,#3f7a12 60%,#333)}
.video{left:154px;top:745px;width:363px;height:202px;border:3px solid var(--orange);background:radial-gradient(ellipse at 50% 45%,#6c6f76,#25272c 70%)}
.video svg{position:absolute;left:159px;top:71px}
.video-caption{left:165px;top:955px;font-size:12.5px;line-height:15.6px}
.features{left:535px;top:744px;width:508px;height:288px;border:3px solid var(--orange)}
.feature{position:absolute;left:5px;width:485px;border-bottom:1px solid #e4e4e4}
.feature svg{position:absolute;left:3px}
.feature h3{position:absolute;left:69px;top:0;font-size:12.5px;color:var(--orange);font-weight:700}
.feature p{position:absolute;left:69px;top:15px;font-size:12.5px;line-height:15.6px;color:var(--ink-soft)}
.portrait{left:155px;top:1049px;width:102px;height:102px;border:3px solid var(--orange);background:linear-gradient(#f3f3f3,#d6d6d6)}
.quote-mark{font-size:84px;font-weight:700;color:var(--orange);line-height:1}
.testimonial{left:313px;top:1068px;font-size:12.5px;line-height:15.6px}
.testimonial .first{padding-left:5px}
.testimonial-author{left:313px;top:1133px;font-size:12.5px;font-weight:700}
.footer{left:154px;top:1168px;width:892px;height:172px;background:var(--footer)}
.col{position:absolute;top:8px;width:205px}
.col h4{font-size:12.5px;color:var(--orange);font-weight:700;padding:0 0 6px 3px;border-bottom:1px solid var(--rule);margin-bottom:8px}
.col p{font-size:12.5px;line-height:15.6px;color:var(--ink-soft)}
.col .contact{padding-bottom:6px;border-bottom:1px solid var(--rule)}
.social{position:absolute;top:108px;width:43px;height:43px;border-radius:4px}
.bottom-bar{left:158px;top:1344px;width:883px;height:46px;background:linear-gradient(var(--orange-light),var(--orange));color:#fff;font-size:12px;text-align:center;line-height:42px}
</style>
</head>
<body>
<div class="stage">

  <header>
    <div class="abs logo"><span class="logo-mark"></span><span class="logo-name">durvelo</span></div>
    <div class="abs search"><svg width="10" height="10" viewBox="0 0 10 10"><circle cx="4" cy="4" r="3" fill="none" stroke="#fff" stroke-width="1.4"/><path d="M6.3 6.3 9 9" stroke="#fff" stroke-width="1.6"/></svg></div>
    <nav class="abs nav">
      <a style="left:66px">Hot Product</a>
      <a class="active" style="left:139px">Screen Protector</a>
      <a style="left:277px">Videos</a>
      <a style="left:341px">Contact us</a>
      <a style="left:426px">About us</a>
    </nav>
    <div class="abs newsletter-input">name@email.com<svg width="10" height="10" viewBox="0 0 10 10"><circle cx="4" cy="4" r="3" fill="none" stroke="#fff" stroke-width="1.4"/><path d="M6.3 6.3 9 9" stroke="#fff" stroke-width="1.6"/></svg></div>
    <div class="abs newsletter-btn">News letter&nbsp; Sign up</div>
  </header>

  <section>
    <div class="abs banner-frame"></div>
    <div class="abs banner">
      <h1>Mobile Applications</h1>
      <p class="lines">This is Photoshop's version&nbsp; of Lorem Ipsum. Proin gravida nibh<br>vel velit auctor aliquet. Aenean sollicitudin, lorem quis bibendum<br>auctor, nisi elit consequat ipsum, nec sagittis sem nibh id elit. Duis<br>sed odio sit amet nibh vulputate cursus a sit amet mauris.</p>
      <div class="btn-download">Download</div>
      <div class="banner-art" role="img" aria-label="Two smartphones showing a cloud app screen"></div>
      <svg class="abs" style="left:0;top:150px" width="30" height="80" viewBox="0 0 30 80"><path d="M0 0C0 20 26 25 26 40S0 60 0 80Z" fill="#fff"/><path d="M13 36 7 40 13 44Z" fill="#bbb"/></svg>
      <svg class="abs" style="left:850px;top:150px" width="30" height="80" viewBox="0 0 30 80"><path d="M30 0C30 20 4 25 4 40S30 60 30 80Z" fill="#fff"/><path d="M17 36 23 40 17 44Z" fill="#bbb"/></svg>
      <svg class="abs" style="left:370px;top:376px" width="140" height="26" viewBox="0 0 140 26"><path d="M0 26C16 26 14 2 34 2H106C126 2 124 26 140 26Z" fill="#fff"/><g fill="#bdbdbd"><circle cx="33" cy="16" r="4"/><circle cx="51" cy="16" r="4"/><circle cx="69" cy="16" r="4"/><circle cx="86" cy="16" r="4"/><circle cx="103" cy="16" r="4"/></g></svg>
    </div>
    <div class="abs banner-shadow"></div>
  </section>

  <section>
    <div class="abs strip"></div>
    <div class="abs strip-inner"></div>
    <div class="tile arrow" style="left:166px"><svg width="30" height="36" viewBox="0 0 30 36"><path d="M24 2 8 18 24 34" fill="none" stroke="#fff" stroke-width="6"/></svg></div>
    <div class="tile thumb" style="left:238px"><span role="img" aria-label="Tablet and phone with screen protector"></span></div>
    <div class="tile thumb" style="left:386px"><span role="img" aria-label="Tablet and phone with screen protector"></span></div>
    <div class="tile thumb" style="left:535px"><span role="img" aria-label="Tablet and phone with screen protector"></span></div>
    <div class="tile thumb" style="left:683px"><span role="img" aria-label="Tablet and phone with screen protector"></span></div>
    <div class="tile thumb" style="left:831px"><span role="img" aria-label="Tablet and phone with screen protector"></span></div>
    <div class="tile arrow" style="left:980px"><svg width="30" height="36" viewBox="0 0 30 36"><path d="M6 2 22 18 6 34" fill="none" stroke="#fff" stroke-width="6"/></svg></div>
  </section>

  <section>
    <div class="abs video" role="img" aria-label="Video still of a person holding up a smartphone">
      <svg width="50" height="50" viewBox="0 0 50 50"><circle cx="25" cy="25" r="23" fill="rgba(255,255,255,.15)" stroke="#fff" stroke-width="3"/><path d="M19 13 37 25 19 37Z" fill="#fff"/></svg>
    </div>
    <p class="abs video-caption lines">This is Photoshop's version&nbsp; of Lorem Ipsum. Proin gravida nibh<br>vel velit auctor aliquet. Aenean sollicitudin, lorem quis biben-<br>dum auctor, nisi elit consequat ipsum, nec sagittis sem nibh id<br>elit. Duis sed odio sit amet nibh vulputate cursus a sit amet</p>

    <div class="abs features">
      <div class="feature" style="top:11px;height:76px">
        <svg style="top:4px" width="56" height="56" viewBox="0 0 56 56"><defs><radialGradient id="globe" cx=".35" cy=".3"><stop offset="0" stop-color="#9fd5ff"/><stop offset="1" stop-color="#2a6fc0"/></radialGradient></defs><circle cx="28" cy="28" r="26" fill="url(#globe)"/></svg>
        <h3>This is Photoshop's version&nbsp; of Lorem Ipsum.</h3>
        <p class="lines">Proin gravida nibh vel velit auctor aliquet. Aenean sollicitudin, lorem quis<br>bibendum auctor, nisi elit consequat ipsum, nec sagittis sem nibh id elit. Duis<br>sed odio sit amet nibh vulputate cursus a sit amet mauris morbi accumsan.</p>
      </div>
      <div class="feature" style="top:97px;height:80px">
        <svg style="top:10px" width="56" height="50" viewBox="0 0 56 50"><path d="M2 28 10 22 20 34 48 4 54 8 21 48Z" fill="#7cc21e"/></svg>
        <h3>This is Photoshop's version&nbsp; of Lorem Ipsum.</h3>
        <p class="lines">Proin gravida nibh vel velit auctor aliquet. Aenean sollicitudin, lorem quis<br>bibendum auctor, nisi elit consequat ipsum, nec sagittis sem nibh id elit. Duis<br>sed odio sit amet nibh vulputate.</p>
      </div>
      <div class="feature" style="top:191px;height:78px">
        <svg style="top:2px" width="56" height="56" viewBox="0 0 56 56"><circle cx="28" cy="28" r="26" fill="#6d8fc4"/><circle cx="28" cy="28" r="21" fill="#fff"/><path d="M28 12V28H38" fill="none" stroke="#333" stroke-width="2"/></svg>
        <h3>This is Photoshop's version&nbsp; of Lorem Ipsum.</h3>
        <p class="lines">Proin gravida nibh vel velit auctor aliquet. Aenean sollicitudin, lorem quis<br>bibendum auctor, nisi elit consequat ipsum, nec sagittis sem nibh id elit. Duis<br>sed odio sit amet nibh vulputate cursus a sit amet mauris.</p>
      </div>
    </div>
  </section>

  <section>
    <div class="abs portrait" role="img" aria-label="Portrait of the customer quoted"></div>
    <div class="abs quote-mark" style="left:276px;top:1040px">“</div>
    <p class="abs testimonial lines"><span class="first">This is Photoshop's version&nbsp; of Lorem Ipsum. Proin gravida nibh vel velit auctor aliquet. Aenean sollicitudin, lorem quis</span><br>bibendum auctor, nisi elit consequat ipsum, nec sagittis sem nibh id elit. Duis sed odio sit amet nibh vulputate cursus a sit<br>amet mauris. Morbi accumsan ipsum.</p>
    <div class="abs quote-mark" style="left:534px;top:1088px">”</div>
    <p class="abs testimonial-author">- Daniel Marsh, UK</p>
  </section>

  <footer>
    <div class="abs footer">
      <div class="col" style="left:11px"><h4>Popular Links</h4><p class="lines">This is Photoshop's version&nbsp; of Lorem<br>Ipsum. Proin gravida nibh vel velit<br>auctor aliquet. Aenean sollicitudin,<br>lorem quis bibendum auctor, nisi elit<br>consequat ipsum, nec sagittis sem<br>nibh id elit. Duis sed odio sit amet<br>nibh vulputate cursus a sit amet</p></div>
      <div class="col" style="left:232px"><h4>Our Patners</h4><p class="lines">This is Photoshop's version&nbsp; of Lorem<br>Ipsum. Proin gravida nibh vel velit<br>auctor aliquet. Aenean sollicitudin,<br>lorem quis bibendum auctor, nisi elit<br>consequat ipsum, nec sagittis sem<br>nibh id elit. Duis sed odio sit amet<br>nibh vulputate cursus a sit amet</p></div>
      <div class="col" style="left:454px"><h4>Popular Links</h4><p class="lines">This is Photoshop's version&nbsp; of Lorem<br>Ipsum. Proin gravida nibh vel velit<br>auctor aliquet. Aenean sollicitudin,<br>lorem quis bibendum auctor, nisi elit<br>consequat ipsum, nec sagittis sem<br>nibh id elit. Duis sed odio sit amet<br>nibh vulputate cursus a sit amet</p></div>
      <div class="col" style="left:675px"><h4>Stay in contact with us</h4><p class="lines contact">Official Address,<br>This is Photoshop's version&nbsp; of Lorem<br>Ipsum. Proin gravida nibh vel velit</p>
        <span class="social" style="left:3px;background:#f5b321"></span>
        <span class="social" style="left:77px;background:#7cc8ec"></span>
        <span class="social" style="left:150px;background:#3b5ea8"></span>
      </div>
    </div>
    <div class="abs bottom-bar">All right reserved | copyright 2013</div>
  </footer>

</div>
</body>
</html>
```